6 page suburb profile/report for real estate agent to provide to clients

I would like a suburb report to be created in our corporate colours and branding for a local Geelong (Australia) based real estate agent.

The design should be fresh, clean and easy to read, not to cluttered. I dont want a corporate plain boring style.

All content and details are provided and the below link provides a bunch of stock photos that can be used. If you prefer to source some better images from pixmarla or framovendix im happy for them to be ripped and used as low res and if you win the job i will then purchase the images and supply hi res.

I have also included a couple of sample reports produced by other organisations and style/brand guides for our corporation.

The word doc attached has all content to be included and also some notes for your reference. There are a variety of charts to be created (all data provided in word doc), the notes indicating the type/style of chart to be used is a guide only. If you feel you can create a better design/layout using different formats/styles thats fine by me.

If you win the job i will need a further 12 reports produced using the style/format. It will be a case of updating the stats/figures for each report.

If you have any questions regarding the project please dont hesitate to contact me.

6 page document
Page size: A4 Portrait (297mm H x210mm W)
Bleed design off the page
Artwork to setup 100% CMYK
Print ready PDF and live/working files to be supplied
Attached are specs for a variety of programs depending on what you create the job in.
I will require a high res file for printing and also a lower res file suitebale for emailing to clients
Revisions will be required before final files supplied

Stock images
https://www.filvornex.com/sh/qu7ra2bn4lo8tpx/BBRWQKEz7LM41Xo9Vp_J8dh?dl=0

Target Market(s)

Property owners, property investors, people interested in buying and selling property

Industry/Entity Type

Real Estate Agent

Font styles to use
Serif
Sans Serif
Other font styles liked:
• Source Sans Pro is the corporate font

Colors
0692cd
33a6d7
85cae6
cee9f5
cdddec
85abd2
3176b5
0355a3

Requirements
Must have
• Statistical content provided
• Corporate logo
• Corporate colours - can be creative but dont want a birght happy colour rainbow of colours
Should not have
• Must not represent other real estate agencies corporate colours

```html
<!DOCTYPE html>
<html lang="en">
<head>
<meta charset="utf-8">
<title>Hamlyn Heights VIC 3215 – Suburb Insights</title>
<link rel="stylesheet" href="https://fonts.googleapis.com/css2?family=Bodoni+Moda:wght@400;500&family=Lato:wght@400;700&display=swap">
<style>
  :root {
    --navy: #0355a3;
    --deep: #0a4a8a;
    --mid-blue: #3176b5;
    --ocean: #0692cd;
    --sky: #33a6d7;
    --pale: #85cae6;
    --ice: #cee9f5;
    --steel: #85abd2;
    --mist: #cdddec;
    --ink: #55585e;
    --page-grey: #d5d8dc;
  }
  * { box-sizing: border-box; margin: 0; padding: 0; }
  html, body { width: 900px; height: 1200px; overflow: hidden; }
  body {
    position: relative;
    font-family: "Bodoni Moda", "Times New Roman", serif;
    color: var(--ink);
    background: linear-gradient(90deg, var(--page-grey) 0%, #ececee 35%, #ffffff 65%);
  }
  .top-decor { position: absolute; left: 0; top: 0; }
  .suburb-map {
    position: absolute; left: 665px; top: 26px; width: 188px; height: 172px;
    background: #fff; border: 2px solid var(--mid-blue); padding: 6px;
    box-shadow: 0 2px 6px rgba(0,0,0,.25);
  }
  .suburb-map div {
    width: 100%; height: 100%;
    background: linear-gradient(135deg, #efe6dc 0%, #ece3d6 55%, #cfe3bf 80%, #bfdcb0 100%);
  }
  .title {
    position: absolute; left: 45px; top: 132px;
    font-size: 33px; font-weight: 400; color: #1f3556; letter-spacing: -.3px;
  }
  .title .postcode { color: var(--ocean); margin-left: 12px; }
  .subtitle {
    position: absolute; left: 45px; top: 182px;
    font-size: 27px; font-weight: 400; color: var(--sky);
  }
  .intro {
    position: absolute; left: 45px; top: 226px; width: 792px;
    font-size: 20.5px; line-height: 33px; text-align: justify;
  }
  .num { color: var(--navy); }
  .section-tab {
    position: absolute; left: 0; width: 318px; height: 46px;
    background: linear-gradient(90deg, #3a8fc4, #2d86bf);
    clip-path: polygon(0 0, 100% 0, 92% 100%, 0 100%);
    border-top: 6px solid var(--navy);
    color: #fff; font-size: 23px; padding-left: 68px; line-height: 38px;
  }
  .tab-demographics { top: 533px; }
  .tab-population { top: 945px; }
  .tab-population { padding-left: 78px; }
  .chart-panel { position: absolute; left: 67px; top: 600px; }
  .divider {
    position: absolute; left: 289px; top: 606px; width: 3px; height: 295px;
    background: var(--navy);
  }
  .stats {
    position: absolute; left: 378px; font-size: 21px; line-height: 32px; color: var(--ink);
  }
  .stats .num { margin-left: 12px; }
  .stats-dwelling { top: 598px; }
  .stats-tenure { top: 760px; }
  .chart-placeholder {
    position: absolute; left: 0; width: 900px; top: 1074px;
    text-align: center; font-size: 21px; color: #222;
  }
  .bottom-band { position: absolute; left: 0; top: 1155px; }
</style>
</head>
<body>

<svg class="top-decor" width="900" height="110" viewBox="0 0 900 110">
  <defs>
    <linearGradient id="greyBand" x1="0" x2="1" y1="0" y2="0">
      <stop offset="0" stop-color="#a9b9c6"/>
      <stop offset="1" stop-color="#e3e9ee"/>
    </linearGradient>
    <linearGradient id="cyanBand" x1="0" x2="1" y1="0" y2="0">
      <stop offset="0" stop-color="#e4f3fa"/>
      <stop offset="1" stop-color="#bfe3f2"/>
    </linearGradient>
  </defs>
  <polygon points="0,0 680,0 0,98" fill="url(#greyBand)"/>
  <polygon points="60,0 680,0 690,78" fill="url(#cyanBand)"/>
  <polygon points="620,0 900,0 900,82" fill="#4f7cc4"/>
</svg>

<div class="suburb-map"><div role="img" aria-label="Street map of Hamlyn Heights"></div></div>

<h1 class="title">Hamlyn Heights<span class="postcode">VIC 3215</span></h1>
<h2 class="subtitle">Suburb Insights</h2>

<p class="intro">The size of Hamlyn Heights is approximately <span class="num">4</span> square kilometres. It has <span class="num">6</span> parks covering nearly <span class="num">3%</span> of total area. The population of Hamlyn Heights in <span class="num">2006</span> was <span class="num">5,838</span> people, by <span class="num">2011</span> the population was <span class="num">6,078</span> showing a population growth of <span class="num">4%</span> in the area during that time. Households in Hamlyn Heights are primarily couples with children and are likely to be repaying between <span class="num">$1400-$1800</span> per month on mortgage repayments. In <span class="num">2011</span> <span class="num">74%</span> of homes were owner-occupied, slightly down when compared to <span class="num">75.3%</span> in <span class="num">2006</span>.</p>

<div class="section-tab tab-demographics">Demographics</div>

<svg class="chart-panel" width="211" height="313" viewBox="0 0 211 313" font-family="Lato, Arial, sans-serif" font-size="9.5" fill="#0a3a6e">
  <defs>
    <linearGradient id="panelFill" x1="0" x2="1" y1="0" y2="1">
      <stop offset="0" stop-color="#7fb0d3"/>
      <stop offset="1" stop-color="#a7cfe3"/>
    </linearGradient>
  </defs>
  <rect width="211" height="313" fill="url(#panelFill)"/>
  <!-- dwelling type -->
  <path d="M95,72 L155,72 A60,60 0 0,1 151.7,91.5 Z" fill="#a9d4ea"/>
  <path d="M95,72 L151.7,91.5 A60,60 0 0,1 141.3,110.2 Z" fill="#2e86b5"/>
  <path d="M95,72 L141.3,110.2 A60,60 0 1,1 155,72 Z" fill="#0a4a8a"/>
  <text x="8" y="34">House</text><text x="8" y="45">89 %</text>
  <text x="157" y="82">FLAT</text><text x="157" y="93">5.3 %</text>
  <text x="137" y="115">Semi Det</text><text x="141" y="126">5.7%</text>
  <line x1="0" y1="145" x2="211" y2="145" stroke="#0a4a8a" stroke-width="2"/>
  <!-- tenure -->
  <path d="M95,223 L154.8,228.2 A60,60 0 0,1 154.6,229.7 Z" fill="#a9d4ea"/>
  <path d="M95,223 L154.6,229.7 A60,60 0 0,1 153.9,234.6 Z" fill="#3d5f86"/>
  <path d="M95,223 L153.9,234.6 A60,60 0 0,1 95.4,283 Z" fill="#2e86b5"/>
  <path d="M95,223 L95.4,283 A60,60 0 0,1 43.5,192.2 Z" fill="#14679c"/>
  <path d="M95,223 L43.5,192.2 A60,60 0 0,1 154.8,228.2 Z" fill="#0a4a8a"/>
  <text x="105" y="159" text-anchor="middle">Own 42.8%</text>
  <text x="156" y="222" font-size="8.5">other 0.4%</text>
  <text x="159" y="236" font-size="8.5">Rent Gov</text><text x="159" y="246" font-size="8.5">1.3%</text>
  <text x="4" y="254">Purch</text><text x="4" y="265">33.7%</text>
  <text x="140" y="276">Rent pri 21.8%</text>
</svg>
<div class="divider"></div>

<div class="stats stats-dwelling">
  <p>Separate house:<span class="num">2142</span></p>
  <p>Semi-detached (row/terrace):<span class="num">137</span></p>
  <p>Flat, unit or apartment:<span class="num">128</span></p>
  <p>Other:<span class="num">0</span></p>
</div>

<div class="stats stats-tenure">
  <p>Own:<span class="num">996</span></p>
  <p>Purchasing:<span class="num">783</span></p>
  <p>Rent government:<span class="num">30</span></p>
  <p>Rent private:<span class="num">507</span></p>
  <p>Other:<span class="num">10</span></p>
</div>

<div class="section-tab tab-population">Population</div>

<p class="chart-placeholder">Space for your bar chart</p>

<svg class="bottom-band" width="900" height="45" viewBox="0 0 900 45">
  <defs>
    <linearGradient id="footFill" x1="0" x2="1" y1="0" y2="0">
      <stop offset="0" stop-color="#6fa6c9"/>
      <stop offset="1" stop-color="#b9dcec"/>
    </linearGradient>
  </defs>
  <rect width="900" height="45" fill="url(#footFill)"/>
  <polygon points="392,0 900,0 900,45 440,45" fill="#0a55a8"/>
</svg>

</body>
</html>
```